Assessment Report cover design and formatting

This report is for senior executives and provides leaders with detailed insight into their capabilities and skills. The cover should have space for the date and name of the person doing the assessment. We are looking to modernise the report cover design. We would like the report to be our company colours if possible. The work will likely expand once the cover is done to other parts of the report, ie. the format and layout of the report etc.

Company colours:
Primary colours:
• Blue #0D47A1, #115CD0, #90B6ED, #EEf3FB
• Green #0D91A1, #47A10D, #324C196, #0DA11D
Additional colours:
• Purple #A10D91
• Brown #A1670D
• Red #A10D47

Target Market(s)

Executives

Industry/Entity Type

Consulting, leadership development

Colors
0094D4
00A9DD
6FCCEA
C7EBF8
E9F6FB
00AB8E
00BBA5
67D7C9
C6EFE9
E9F9F6
E54698
E96AAD
F1A4CE
F9D9EA
FCEFF6
6B429C
8869AF
B7A5CE
E3DAEB
F3F0F8

Requirements
Must have
• The report cover should have space for name of user, the date and company logo. Cover should be in A4 size.

```html
<!DOCTYPE html>
<html lang="en">
<head>
<meta charset="utf-8">
<title>Growth Leader Assessment – Insight Report Cover</title>
<link rel="stylesheet" href="https://fonts.googleapis.com/css2?family=Montserrat:ital,wght@0,300;0,500;0,700;1,700&display=swap">
<style>
  :root {
    --backdrop: #939498;
    --paper: #f2f3f6;
    --paper-light: #f7f8fb;
    --purple: #6b429c;
    --pink: #e54698;
    --navy: #1646a0;
    --steel: #3780b8;
    --ink-blue: #1a3f9a;
    --photo-sky: #a9c2e2;
    --photo-mid: #5f7fa8;
    --photo-dark: #263447;
    --white: #ffffff;
  }
  * { margin: 0; padding: 0; box-sizing: border-box; }
  html, body {
    width: 1200px;
    height: 1200px;
    overflow: hidden;
    background: var(--backdrop);
  }
  .report-cover {
    position: absolute;
    left: 198px;
    top: 40px;
    width: 791px;
    height: 1119px;
    box-shadow: 0 0 4px rgba(0,0,0,0.35);
  }
  .report-cover svg { display: block; width: 791px; height: 1119px; }
  .title, .subtitle, .label, .brand-name { font-family: "Montserrat", sans-serif; }
  .title-main { font-weight: 700; fill: var(--white); }
  .title-sub { font-weight: 700; fill: var(--white); }
  .report-kind { font-weight: 300; fill: var(--steel); }
  .report-sample { font-weight: 700; fill: var(--steel); }
  .label { font-weight: 700; font-style: italic; fill: var(--ink-blue); }
  .brand-name { font-weight: 500; fill: var(--ink-blue); }
</style>
</head>
<body>
<main class="report-cover">
  <svg viewBox="0 0 791 1119" xmlns="http://www.w3.org/2000/svg">
    <defs>
      <linearGradient id="paper-fill" x1="0" y1="0" x2="1" y2="1">
        <stop offset="0" stop-color="var(--paper)"/>
        <stop offset="1" stop-color="var(--paper-light)"/>
      </linearGradient>
      <linearGradient id="photo-fill" x1="0.7" y1="0" x2="0.3" y2="1">
        <stop offset="0" stop-color="var(--photo-sky)"/>
        <stop offset="0.5" stop-color="var(--photo-mid)"/>
        <stop offset="1" stop-color="var(--photo-dark)"/>
      </linearGradient>
      <linearGradient id="footer-fill" x1="0" y1="0" x2="1" y2="0">
        <stop offset="0" stop-color="var(--navy)"/>
        <stop offset="0.5" stop-color="var(--steel)"/>
        <stop offset="1" stop-color="var(--navy)"/>
      </linearGradient>
    </defs>

    <!-- paper -->
    <rect class="paper" width="791" height="1119" fill="url(#paper-fill)"/>

    <!-- hero photo area -->
    <rect class="hero-photo" x="0" y="163" width="791" height="458" fill="url(#photo-fill)"
          role="img" aria-label="Upward view of glass office skyscrapers against a pale blue sky"/>

    <!-- geometric accents -->
    <polygon class="accent-purple" points="0,40 360,40 0,382" fill="var(--purple)"/>
    <polygon class="accent-pink" points="360,40 567,163 231,163" fill="var(--pink)"/>
    <polygon class="accent-steel" points="424,621 666,621 571,712" fill="var(--steel)"/>
    <polygon class="accent-navy" points="791,502 791,712 571,712" fill="var(--navy)"/>

    <!-- brand -->
    <g class="brand">
      <circle cx="562" cy="84" r="9" fill="var(--ink-blue)"/>
      <text class="brand-name" x="735" y="93" font-size="25" text-anchor="end">Meridian</text>
      <text class="brand-name" x="735" y="124" font-size="25" text-anchor="end">Advisory</text>
    </g>

    <!-- title -->
    <text class="title title-main" x="132" y="387" font-size="118" textLength="508" lengthAdjust="spacingAndGlyphs">Growth</text>
    <text class="title title-sub" x="132" y="450" font-size="62" textLength="615" lengthAdjust="spacingAndGlyphs">Leader Assement</text>

    <!-- report type -->
    <text class="subtitle report-kind" x="66" y="766" font-size="47" textLength="377" lengthAdjust="spacingAndGlyphs">INSIGHT REPORT</text>
    <text class="subtitle report-sample" x="66" y="832" font-size="62" textLength="264" lengthAdjust="spacingAndGlyphs">SAMPLE</text>
    <rect class="title-rule" x="66" y="871" width="151" height="9" rx="4.5" fill="var(--pink)"/>

    <!-- assessment details -->
    <rect class="detail-marker" x="351" y="958" width="15" height="15" fill="var(--pink)"/>
    <text class="label" x="660" y="972" font-size="19" text-anchor="end">Prepared by</text>
    <line x1="662" y1="977" x2="912" y2="977" stroke="var(--pink)" stroke-width="1.3"/>
    <text class="label" x="654" y="1008" font-size="19" text-anchor="end">Date</text>
    <line x1="662" y1="1009" x2="912" y2="1009" stroke="var(--pink)" stroke-width="1.3"/>

    <!-- footer band -->
    <rect class="footer-band" x="0" y="1043" width="791" height="76" fill="url(#footer-fill)"/>
  </svg>
</main>
</body>
</html>
```